Reshape my sector - Site for startup to grow

Update: To clarify I've started a few wireframes: http://snipr.example/7qk3zWd this is by no means complete or even the layout im looking for, just some idea of the elements on the first few pages

This is for design only, I require PSDs as well high res versions of logo/other asset.

Concept

The site is place where Domain experts to identify real world problems in there respective industries that could be solved with software or hard ward products.

A similar site to this is : http://www.notionharbor.example/ which allows anyone to suggest ideas for products they want realising.

Pages needing design:

1) Login

2) Problems search: List of problems posted filterable by industry. Should contain:

- User who posted the problem (name, picture, etc)
- Title and short description of the problem space
- Current state of the project i.e. team created, just started, etc.

3) Problem details page, should contain:

- Title and large description of the problem space
- Optional image
- List of products that attempt to solve the problem (Name of product, short description, url)
- Discussion board (small forum for discussing the idea)
- List of teams started to solve the problem (show number of members and current state of the team, link to public team page)

4) Post a problem page:

- Form to create a problem containing all the things above

4) Public team page

- Shows team members (name, position, link to bio)
- List of team blog posts
- Adverts for team members, funding partners, beta testers etc

5) Private team page

- The ability to change the status of the project
- The ability to post blogs promoting there project
- The ability to advertise for additional team member, funding
partners, beta testers etc
- Private discussion board

The site will be called "www.reshapemysector.example" and will require a logo.

Target Market(s)

software developers, designers, entrepreneurs, VCs

Industry/Entity Type

Industry

Number of Pages Required

5+ page

Font styles to use
Serif
Sans Serif

Requirements
Must have
• PSDs + high res images
• Simple clean design see:
• - https://trial.velvetboards.example/
• - https://talk.quillnest.example/
• - https://pinmosaic.example/shots/4830517-Task-Panel/attachments/395208

```html
<!DOCTYPE html>
<html lang="en">
<head>
<meta charset="utf-8">
<title>Reshape my sector – Problems</title>
<link rel="stylesheet" href="https://fonts.googleapis.com/css2?family=Jost:wght@300;400;500;600&display=swap">
<style>
:root{
  --side-top:#2caede;
  --side-bottom:#1769b5;
  --side-text:#ffffff;
  --side-muted:rgba(255,255,255,.55);
  --side-panel:rgba(255,255,255,.12);
  --page:#eef2f7;
  --card:#ffffff;
  --accent:#1ea3d8;
  --number:#3b6fd1;
  --ink:#3a3f47;
  --soft:#8b9098;
  --dot-blue:#5a80e2;
  --dot-dark:#2f3a48;
  --badge:#f39a1e;
  --line:#e3e8ef;
}
*{box-sizing:border-box;margin:0;padding:0}
html,body{width:1200px;height:696px;overflow:hidden;background:var(--page)}
body{font-family:"Jost",sans-serif;color:var(--ink);position:relative}

/* Sidebar */
.sidebar{position:absolute;left:0;top:0;width:223px;height:696px;
  background:linear-gradient(180deg,var(--side-top),var(--side-bottom));color:var(--side-text)}
.brand{position:absolute;left:25px;top:18px;display:flex;align-items:center;gap:12px}
.brand-mark{width:28px;height:28px;border-radius:50%;background:var(--side-text)}
.brand-name{font-size:15px;font-weight:500;line-height:16px;letter-spacing:.3px;text-transform:uppercase}
.nav-item{position:absolute;left:25px;display:flex;align-items:center;gap:14px;
  font-size:11px;font-weight:500;letter-spacing:.3px;text-transform:uppercase}
.nav-item svg{width:14px;height:14px;fill:currentColor}
.nav-item.muted{color:var(--side-muted)}
.nav-sub{position:absolute;left:55px;font-size:10.5px;text-transform:uppercase}
.nav-sub.muted{color:var(--side-muted)}
.nav-count{position:absolute;left:181px;width:14px;height:14px;border-radius:50%;
  background:var(--badge);font-size:8px;text-align:center;line-height:14px;color:#fff}
.update-panel{position:absolute;left:25px;top:304px;width:171px;height:104px;background:var(--side-panel);border-radius:2px;padding:16px 18px}
.update-user{display:flex;align-items:center;gap:8px}
.update-avatar{width:28px;height:28px;border-radius:50%;background:linear-gradient(135deg,#6d6a6a,#2b2e33)}
.update-name{font-size:10px;font-weight:500;line-height:10px}
.update-role{font-size:7px;opacity:.8}
.update-text{margin-top:14px;font-size:8.5px;line-height:14px}
.side-button{position:absolute;top:632px;width:81px;height:47px;background:var(--side-panel);border-radius:2px;
  display:flex;align-items:center;justify-content:center}
.side-button svg{width:15px;height:15px;fill:var(--side-text)}

/* Top bar */
.post-button{position:absolute;left:261px;top:19px;width:226px;height:28px;border-radius:14px;background:var(--accent);
  color:#fff;font-size:11px;font-weight:500;text-transform:uppercase;text-align:center;line-height:28px}
.add-button{position:absolute;left:501px;top:20px;width:27px;height:27px;border-radius:50%;background:var(--number);
  color:#fff;font-size:18px;text-align:center;line-height:26px;font-weight:300}
.select{position:absolute;top:19px;height:28px;background:#fff;border-radius:2px;padding:0 12px;
  display:flex;align-items:center;justify-content:space-between;font-size:12px;color:var(--accent)}
.select svg{width:9px;height:9px;stroke:var(--soft);fill:none;stroke-width:1.5}
.select-menu{position:absolute;left:711px;top:47px;width:129px;height:82px;background:#fff;padding:6px 12px;z-index:2;
  box-shadow:0 4px 10px rgba(40,60,90,.06)}
.select-menu li{list-style:none;font-size:11px;color:var(--soft);line-height:28px}
.search{position:absolute;left:885px;top:19px;width:173px;height:28px;border-radius:14px;background:#fff;
  display:flex;align-items:center;gap:8px;padding:0 12px;font-size:8px;color:#b9bec6}
.search svg{width:11px;height:11px;stroke:#b9bec6;fill:none;stroke-width:1.6}
.user{position:absolute;left:1083px;top:19px;display:flex;align-items:center;gap:12px;font-size:12px;color:var(--number)}
.user-avatar{width:28px;height:28px;border-radius:50%;background:linear-gradient(135deg,#9b6d55,#3b2c27)}

/* Cards */
.problem-grid{position:absolute;left:262px;top:66px;display:grid;grid-template-columns:repeat(3,269px);
  grid-template-rows:repeat(2,307px);column-gap:42px;row-gap:13px}
.problem-card{position:relative;background:var(--card);text-align:center}
.card-tags{position:absolute;top:17px;left:30px;right:30px;display:flex;justify-content:space-between;font-size:9.5px}
.tag{display:flex;align-items:center;gap:8px}
.tag::before{content:"";width:9px;height:9px;border-radius:50%;background:var(--dot-blue)}
.tag.stage::before{background:var(--dot-dark)}
.ribbon{position:absolute;left:7px;top:0;width:13px;height:44px;background:var(--badge);
  clip-path:polygon(0 0,100% 0,100% 84%,50% 100%,0 84%)}
.ribbon span{position:absolute;left:2px;top:3px;writing-mode:vertical-rl;transform:rotate(180deg);
  font-size:6px;color:#fff;letter-spacing:.3px;height:32px;text-align:right}
.avatar{position:absolute;left:50%;top:45px;width:56px;height:56px;margin-left:-28px;border-radius:50%}
.poster-name{position:absolute;top:108px;left:0;right:0;font-size:21px;font-weight:600;color:var(--accent);letter-spacing:.2px;text-transform:uppercase}
.poster-role{position:absolute;top:135px;left:0;right:0;font-size:11.5px}
.card-meta{position:absolute;top:158px;left:30px;right:30px;display:flex;justify-content:space-between;text-align:left}
.stars{font-size:10px;color:var(--number);letter-spacing:1px;line-height:14px}
.topic{font-size:11.5px;text-transform:uppercase}
.start{text-align:center}
.start-label{font-size:9.5px;color:var(--number);text-transform:uppercase;line-height:14px}
.start-date{font-size:12.5px;letter-spacing:.6px}
.summary{position:absolute;top:210px;left:40px;right:40px;font-size:7.5px;line-height:12.5px;color:var(--soft)}
.stats{position:absolute;top:265px;left:22px;right:22px;display:flex;justify-content:space-between}
.stat{width:60px}
.stat b{display:block;font-weight:400;font-size:12px;color:var(--number)}
.stat small{font-size:7px;color:var(--soft)}

.scrollbar{position:absolute;left:1172px;top:170px;width:3px;height:312px;background:#dfe4eb;border-radius:2px}
</style>
</head>
<body>

<aside class="sidebar">
  <div class="brand"><span class="brand-mark"></span><span class="brand-name">Reshape<br>my sector</span></div>

  <div class="nav-item" style="top:112px"><svg viewBox="0 0 16 16"><circle cx="8" cy="9" r="5"/><rect x="1" y="8" width="14" height="1.6"/><rect x="6" y="1" width="4" height="3"/></svg>Problems</div>
  <div class="nav-sub muted" style="top:150px">Latest</div>
  <div class="nav-sub" style="top:188px">Trending</div>
  <div class="nav-sub muted" style="top:225px">Top rated</div>
  <div class="nav-item muted" style="top:262px"><svg viewBox="0 0 16 16"><path d="M2 1h12v10l-4 4H2z"/></svg>News</div>

  <div class="update-panel">
    <div class="update-user">
      <div class="update-avatar" role="img" aria-label="Portrait photo of John Doe"></div>
      <div><div class="update-name">JOHN DOE</div><div class="update-role">team member</div></div>
    </div>
    <p class="update-text">A new Research has been made.<br>Find out about it.</p>
  </div>

  <div class="nav-item muted" style="top:435px"><svg viewBox="0 0 16 16"><path d="M1 3h14v10H1z M1 3l7 6 7-6" fill="none" stroke="currentColor" stroke-width="1.6"/></svg>Messages</div>
  <span class="nav-count" style="top:435px">5</span>
  <div class="nav-item muted" style="top:472px"><svg viewBox="0 0 16 16"><path d="M8 1c3 0 4.5 2.5 4.5 5v4l2 2H1.5l2-2V6C3.5 3.5 5 1 8 1z"/><circle cx="8" cy="14.5" r="1.5"/></svg>Notifications</div>
  <span class="nav-count" style="top:472px">3</span>
  <div class="nav-item muted" style="top:512px"><svg viewBox="0 0 16 16"><circle cx="8" cy="5" r="4"/><path d="M1 16c0-4 3-6 7-6s7 2 7 6z"/></svg>Profile</div>
  <div class="nav-item muted" style="top:552px"><svg viewBox="0 0 16 16"><circle cx="8" cy="8" r="6" fill="none" stroke="currentColor" stroke-width="1.6" stroke-dasharray="5 2.5"/></svg>Team profile</div>

  <div class="side-button" style="left:25px"><svg viewBox="0 0 16 16"><path d="M8 0l1.5 2.5 2.8-.7.7 2.8L15.5 6 14 8l1.5 2-2.5 1.4-.7 2.8-2.8-.7L8 16l-1.5-2.5-2.8.7-.7-2.8L.5 10 2 8 .5 6 3 4.6l.7-2.8 2.8.7z"/><circle cx="8" cy="8" r="2.5" fill="#2a8fcf"/></svg></div>
  <div class="side-button" style="left:115px"><svg viewBox="0 0 16 16"><path d="M6 2H2v12h4" fill="none" stroke="#fff" stroke-width="1.8"/><path d="M6 7h6V4l4 4-4 4V9H6z"/></svg></div>
</aside>

<div class="post-button">Solve our problem</div>
<div class="add-button">+</div>
<div class="select" style="left:573px;width:133px">Chemical<svg viewBox="0 0 10 10"><path d="M1 3l4 4 4-4"/></svg></div>
<div class="select" style="left:711px;width:129px">Stage<svg viewBox="0 0 10 10"><path d="M1 3l4 4 4-4"/></svg></div>
<ul class="select-menu"><li>Just Started</li><li>Team Formed</li><li>Business Formed</li></ul>
<div class="search"><svg viewBox="0 0 12 12"><circle cx="5" cy="5" r="3.8"/><path d="M8 8l3.5 3.5"/></svg>Search</div>
<div class="user"><div class="user-avatar" role="img" aria-label="Portrait photo of John"></div>John</div>

<main class="problem-grid">
  <article class="problem-card">
    <div class="card-tags"><span class="tag">Chemical</span><span class="tag stage">Team Started</span></div>
    <div class="avatar" role="img" aria-label="Portrait photo of Mathew Jackson" style="background:linear-gradient(135deg,#a88070,#3e3330)"></div>
    <h2 class="poster-name">Mathew Jackson</h2>
    <p class="poster-role">Current Position: Chief Scientist at Norvale Tech</p>
    <div class="card-meta"><div><div class="stars">★★★★★</div><div class="topic">Cure cancer</div></div><div class="start"><div class="start-label">Start date</div><div class="start-date">20/09/2016</div></div></div>
    <p class="summary">Nulla semper ultrices tincidunt. Nulla ac convallis diam. Cras leo augue, molestie at leo vel, gravida euismod quam.</p>
    <div class="stats"><div class="stat"><b>1061</b><small>Following</small></div><div class="stat"><b>983</b><small>Teams</small></div><div class="stat"><b>4190</b><small>Discussions</small></div></div>
  </article>

  <article class="problem-card">
    <div class="ribbon"><span>HOT</span></div>
    <div class="card-tags"><span class="tag">Chemical</span><span class="tag stage">Team Started</span></div>
    <div class="avatar" role="img" aria-label="Portrait photo of Phill Jones" style="background:linear-gradient(135deg,#e8e3dd,#4a3f39)"></div>
    <h2 class="poster-name">Phill Jones</h2>
    <p class="poster-role">Current Position: Chief Scientist at Norvale Tech</p>
    <div class="card-meta"><div><div class="stars">★★★★★</div><div class="topic">Cure cancer</div></div><div class="start"><div class="start-label">Start date</div><div class="start-date">20/09/2016</div></div></div>
    <p class="summary">Nulla semper ultrices tincidunt. Nulla ac convallis diam. Cras leo augue, molestie at leo vel, gravida euismod quam.</p>
    <div class="stats"><div class="stat"><b>53</b><small>Following</small></div><div class="stat"><b>18</b><small>Teams</small></div><div class="stat"><b>352</b><small>Discussions</small></div></div>
  </article>

  <article class="problem-card">
    <div class="card-tags"><span class="tag">Chemical</span><span class="tag stage">Team Started</span></div>
    <div class="avatar" role="img" aria-label="Portrait photo of Jacob Dean" style="background:linear-gradient(135deg,#6b5248,#1f1d1f)"></div>
    <h2 class="poster-name">Jacob Dean</h2>
    <p class="poster-role">Current Position: Scientist at Norvale Tech</p>
    <div class="card-meta"><div><div class="stars">★★★☆☆</div><div class="topic">Cure cancer</div></div><div class="start"><div class="start-label">Start date</div><div class="start-date">20/09/2016</div></div></div>
    <p class="summary">Nulla semper ultrices tincidunt. Nulla ac convallis diam. Cras leo augue, molestie at leo vel, gravida euismod quam.</p>
    <div class="stats"><div class="stat"><b>75</b><small>Following</small></div><div class="stat"><b>24</b><small>Teams</small></div><div class="stat"><b>542</b><small>Discussions</small></div></div>
  </article>

  <article class="problem-card">
    <div class="ribbon"><span>TRENDING</span></div>
    <div class="card-tags"><span class="tag">Chemical</span><span class="tag stage">Team Started</span></div>
    <div class="avatar" role="img" aria-label="Portrait photo of Lilly Steward" style="background:linear-gradient(135deg,#c9a898,#2a2222)"></div>
    <h2 class="poster-name">Lilly Steward</h2>
    <p class="poster-role">Current Position: Chief Surgeon at Brightmoor Clinic</p>
    <div class="card-meta"><div><div class="stars">★★★★☆</div><div class="topic">Cure cancer</div></div><div class="start"><div class="start-label">Start date</div><div class="start-date">20/09/2016</div></div></div>
    <p class="summary">Nulla semper ultrices tincidunt. Nulla ac convallis diam. Cras leo augue, molestie at leo vel, gravida euismod quam.</p>
    <div class="stats"><div class="stat"><b>159</b><small>Following</small></div><div class="stat"><b>90</b><small>Teams</small></div><div class="stat"><b>768</b><small>Discussions</small></div></div>
  </article>

  <article class="problem-card">
    <div class="card-tags"><span class="tag">Chemical</span><span class="tag stage">Team Started</span></div>
    <div class="avatar" role="img" aria-label="Portrait photo of Dave O'Brian" style="background:linear-gradient(135deg,#d8d6d4,#262628)"></div>
    <h2 class="poster-name">Dave O’Brian</h2>
    <p class="poster-role">Current Position: Researcher at Corwen Labs</p>
    <div class="card-meta"><div><div class="stars">★★☆☆☆</div><div class="topic">Cure cancer</div></div><div class="start"><div class="start-label">Start date</div><div class="start-date">20/09/2016</div></div></div>
    <p class="summary">Nulla semper ultrices tincidunt. Nulla ac convallis diam. Cras leo augue, molestie at leo vel, gravida euismod quam.</p>
    <div class="stats"><div class="stat"><b>02</b><small>Following</small></div><div class="stat"><b>01</b><small>Teams</small></div><div class="stat"><b>07</b><small>Discussions</small></div></div>
  </article>

  <article class="problem-card">
    <div class="card-tags"><span class="tag">Chemical</span><span class="tag stage">Team Started</span></div>
    <div class="avatar" role="img" aria-label="Portrait photo of Tiffany Mars" style="background:linear-gradient(135deg,#f0d2c4,#a8705a)"></div>
    <h2 class="poster-name">Tiffany Mars</h2>
    <p class="poster-role">Current Position: Scientist at Ashgrove University</p>
    <div class="card-meta"><div><div class="stars">★★★☆☆</div><div class="topic">Cure cancer</div></div><div class="start"><div class="start-label">Start date</div><div class="start-date">20/09/2016</div></div></div>
    <p class="summary">Nulla semper ultrices tincidunt. Nulla ac convallis diam. Cras leo augue, molestie at leo vel, gravida euismod quam.</p>
    <div class="stats"><div class="stat"><b>12</b><small>Following</small></div><div class="stat"><b>06</b><small>Teams</small></div><div class="stat"><b>29</b><small>Discussions</small></div></div>
  </article>
</main>

<div class="scrollbar"></div>
</body>
</html>
```